HR Company Website

Home page and information page needs for Human resources company
SERVICES

Employment Law - -
HR Advice -
Recruitment -
Disciplinaries -
Redundancies -
Coaching & Training -
HR Policy Review -
Contract Writing -
Tribunal Claims -
HR Partner -

LAYOUT SKETCH DISCUSSED:
Yes
On the animation the left hand side messgae banner will be constant along with the button , the right hand side will be animated.

COMPETITION
Vantor HR - www.vantorhr-example.com
Kel HR - www.kelhr-example.co.uk
Brisk HR - www.briskhr-example.com

COMPANY LOGO
Client currently has no logo - Solvinex to design

STRAPLINE:
Brisk HR Partner

ACCREDITATIONS / LOGOS:
Masters Diploma in Emloyment Law

WEBSITE THEME:
Human Resources

MAIN BODY OF WEBSITE:
Light

IMAGES THAT BEST REFLECT YOUR COMPANY:
Staff / Office Based Life style images People groups - no face close ups
planning
infrastructure
NOTHING TOO OBVIOUS

PAGES:

Home
About Us
Our Services
- Employment Law Advice
- HR Advice
- Contracts of Employment
- HR Policies
- Disciplinary Procedures
- Redundancy Advice
Contact Us

MESSAGE BANNERS:
1. 12 Years HR Experience - wealth of experience & knowledge
2. Cost Effective Solution - use us when you need us
3. Personal HR Approach - create bespoke tailored made solutions
4. Preventative Measures Protects - don't leave it until is is too late
5. Complete Peace of Mind - Let us be Brisk HR department

Target Market(s)

Male & Femaie - 30-60

SME Business

Industry/Entity Type

Consulting

Number of Pages Required

2 pages

Requirements
Must have
• This design will be built using the wordpress platform, use the wireframe attached for the layout structure - must be visually impactful - clean and proefessional looking
Nice to have
• I have attached the logo - do not amend the colout but you can add effects onto it if you wish to
Should not have
• Loads of text

```html
<!DOCTYPE html>
<html lang="en">
<head>
<meta charset="utf-8">
<title>Norvane HR Ltd – Home and Inner Page</title>
<link href="https://fonts.googleapis.com/css2?family=Questrial&family=Open+Sans:ital,wght@0,400;0,600;0,700;0,800;1,400&family=Noto+Sans:wght@400;700&display=swap" rel="stylesheet">
<style>
:root{
  --lime:#9ccf1f;
  --green:#1b7a34;
  --green-dark:#0f6a2a;
  --line:#c9c9c9;
  --text:#555;
  --page:#f7f7f7;
}
*{margin:0;padding:0;box-sizing:border-box}
html,body{width:1200px;height:3145px;overflow:hidden}
body{background:var(--page);font-family:"Noto Sans",sans-serif;color:var(--text);position:relative}
.abs{position:absolute}
.page-label{position:absolute;left:0;width:1200px;text-align:center;font-family:"Questrial",sans-serif;font-size:52px;color:var(--lime);letter-spacing:1px;-webkit-text-stroke:1px var(--lime)}
.brand{position:absolute;left:44px;font-family:"Questrial",sans-serif;color:var(--green)}
.brand-name{font-size:46px;line-height:1;display:flex;align-items:center;gap:10px}
.brand-name i{display:inline-block;width:14px;height:14px;background:var(--green);border-radius:50%}
.brand-tag{font-size:19px;margin-left:100px;margin-top:8px}
.call{position:absolute;right:46px;font-family:"Questrial",sans-serif;color:var(--green);font-size:20px}
.call b{font-weight:400;font-size:30px;margin-left:6px}
.nav{position:absolute;right:46px;display:flex;align-items:center;font-family:"Questrial",sans-serif;font-size:20px;color:var(--green)}
.nav a{color:var(--green);text-decoration:none;padding:4px 10px}
.nav .sep{margin:0 8px}
.nav a.active{background:linear-gradient(#444,#111);color:#fff;box-shadow:0 2px 3px rgba(0,0,0,.5)}
.hero{position:absolute;left:0;width:1200px;border-top:3px solid var(--green-dark);background:linear-gradient(120deg,#4aa72f,#6cc13f 55%,#4ca831)}
.hero-side{position:absolute;left:0;top:0;bottom:0;background:linear-gradient(160deg,#6fc444,#4ea532)}
.hero-title{position:absolute;left:50px;color:#fff;font-family:"Open Sans",sans-serif;font-weight:800;font-size:28px;line-height:43px;text-shadow:0 1px 2px rgba(0,0,0,.35)}
.btn-dark{position:absolute;background:linear-gradient(#4a4a4a,#111);color:#fff;font-family:"Open Sans",sans-serif;font-weight:700;text-align:center;border-radius:4px;box-shadow:0 2px 3px rgba(0,0,0,.4)}
.slider{position:absolute;left:438px;top:32px;width:716px;height:387px;background:linear-gradient(#555,#111 70%);border-radius:6px}
.slide-photo{position:absolute;left:36px;top:17px;width:641px;height:308px;background:linear-gradient(135deg,#e9e6e1,#cfc8bf 45%,#d7a88a 55%,#bfb8ae);border:2px solid #888}
.arrow{position:absolute;width:48px;height:46px;background:#4fb232}
.arrow svg{display:block;margin:13px auto}
.slide-caption{position:absolute;left:0;width:100%;top:342px;text-align:center;color:#fff;font-family:"Open Sans",sans-serif;font-weight:700;font-size:20px}
.features{position:absolute;left:0;top:739px;width:1200px;height:254px;background:linear-gradient(#ececec,#f6f6f6)}
.feature{position:absolute;top:24px;width:330px}
.feature h3{font-family:"Questrial",sans-serif;font-weight:400;font-size:19px;color:var(--green);margin-left:28px;margin-bottom:16px}
.feature p{font-size:13px;line-height:16px;color:#555;white-space:nowrap;letter-spacing:.2px}
.more{position:absolute;font-size:11px;font-weight:700;color:#555;text-decoration:underline}
.divider{position:absolute;top:20px;height:215px;border-left:1px dashed #d6d6d6}
.testimonial{position:absolute;left:0;top:993px;width:1200px;height:73px;background:linear-gradient(#5a5a5a,#111 60%,#000);color:#8ed83a;font-family:"Open Sans",sans-serif;font-weight:700;font-size:21px;text-align:center;line-height:73px}
.box{position:absolute;border:2px solid var(--line);border-radius:4px;background:linear-gradient(#fff,#f2f2f2)}
.box h2{font-family:"Questrial",sans-serif;font-weight:400;font-size:23px;color:var(--green);text-align:center;margin-top:18px}
.details{padding:14px 0 0 24px;font-size:12.5px;line-height:16px;color:#555}
.details h4{font-size:12.5px;font-weight:700;letter-spacing:1px;color:#444;margin-top:14px}
.details h4:first-child{margin-top:0}
.details p{margin-top:6px}
.details h4.tight + p{margin-top:0}
.promo{font-family:"Questrial",sans-serif;color:var(--green);font-size:20px;text-align:center;line-height:34px}
.form-sub{font-style:italic;font-size:12.5px;text-align:center;color:#666;margin-top:4px}
.field{position:absolute;left:10px;font-size:12px;font-weight:700;color:#444}
.input{position:absolute;left:94px;width:200px;height:26px;background:#e9e9e9}
.band{position:absolute;left:0;width:1200px;background:linear-gradient(#71c444,#4ea532);border-top:3px solid var(--green-dark);color:#fff;font-family:"Open Sans",sans-serif;font-weight:700;text-align:center}
.crumb{position:absolute;left:0;top:2119px;width:1200px;height:36px;background:linear-gradient(#68b83e,#4b9f31);color:#fff;font-family:"Open Sans",sans-serif;font-weight:700;font-size:13.5px;line-height:36px;padding-left:44px}
.about{position:absolute;left:44px;top:2216px;width:660px}
.about h1{font-family:"Open Sans",sans-serif;font-weight:700;font-size:29px;color:var(--green-dark);margin-left:-2px}
.about p{font-size:13.3px;line-height:24px;color:#666;margin-top:24px;white-space:nowrap;letter-spacing:.3px}
.about p:first-of-type{margin-top:18px}
.news{padding:22px 30px 0 30px;font-size:13.5px;line-height:24px;color:#666}
.news p{margin-bottom:24px}
</style>
</head>
<body>

<!-- ===== Home page ===== -->
<div class="page-label" style="top:36px">HOME PAGE</div>

<div class="brand" style="top:152px">
  <div class="brand-name"><i></i>Norvane HR Ltd</div>
  <div class="brand-tag">Brisk HR Partner</div>
</div>
<div class="call" style="top:170px">CALL NOW: <b>111 4040 727</b></div>
<nav class="nav" style="top:244px">
  <a class="active" href="#">HOME</a>
  <a href="#" style="margin-left:12px">ABOUT US</a><span class="sep">|</span>
  <a href="#">OUR</a><span class="sep">|</span>
  <a href="#">SERVICES</a><span class="sep">|</span>
  <a href="#" style="padding-right:0">CONTACT US</a>
</nav>

<section class="hero" style="top:283px;height:456px">
  <div class="hero-side" style="width:388px"></div>
  <div class="hero-title" style="top:140px">IS YOUR COMPANY<br>LEGALLY COMPLIANT?</div>
  <div class="btn-dark" style="left:67px;top:267px;width:272px;height:36px;line-height:36px;font-size:17px">FREE HR AUDIT</div>
  <div class="slider">
    <div class="slide-photo" role="img" aria-label="Photo of two business people shaking hands"></div>
    <div class="arrow" style="left:14px;top:149px"><svg width="12" height="20" viewBox="0 0 12 20"><path d="M9 3 L3 10 L9 17" stroke="#fff" stroke-width="2" fill="none"/></svg></div>
    <div class="arrow" style="left:650px;top:149px"><svg width="12" height="20" viewBox="0 0 12 20"><path d="M3 3 L9 10 L3 17" stroke="#fff" stroke-width="2" fill="none"/></svg></div>
    <div class="slide-caption">“Complete Peace of Mind - Let us be Brisk HR department”</div>
  </div>
</section>

<section class="features">
  <div class="feature" style="left:44px">
    <h3>Employment Law Advice</h3>
    <p>Lorem ipsum dolor sit amet, consectetur<br>adipiscing elit. Donec nisl magna, congue<br>id ullamcorper quis, faucibus ac diam. Mauris<br>dictum orci vitae neque varius condimentum.<br>Morbi venenatis fringilla risus sed iaculis.<br>Integer luctus orci ac mauris pulvinar id<br>lacinia lorem tincidunt. Suspendisse potenti.<br>Vivamus nec neque sapien.</p>
  </div>
  <div class="divider" style="left:398px"></div>
  <div class="feature" style="left:456px">
    <h3 style="margin-left:34px">Personal HR approach</h3>
    <p>Lorem ipsum dolor sit amet, consectetur<br>adipiscing elit. Donec nisl magna, congue<br>id ullamcorper quis, faucibus ac diam. Mauris<br>dictum orci vitae neque varius condimentum.<br>Morbi venenatis fringilla risus sed iaculis.<br>Integer luctus orci ac mauris pulvinar id<br>lacinia lorem tincidunt. Suspendisse potenti.<br>Vivamus nec neque sapien.</p>
  </div>
  <div class="divider" style="left:797px"></div>
  <div class="feature" style="left:836px">
    <h3 style="margin-left:52px">Rates &amp; Packages</h3>
    <p>Lorem ipsum dolor sit amet, consectetur<br>adipiscing elit. Donec nisl magna, congue<br>id ullamcorper quis, faucibus ac diam. Mauris<br>dictum orci vitae neque varius condimentum.<br>Morbi venenatis fringilla risus sed iaculis.<br>Integer luctus orci ac mauris pulvinar id<br>lacinia lorem tincidunt. Suspendisse potenti.<br>Vivamus nec neque sapien.</p>
  </div>
  <span class="more" style="left:304px;top:210px">More</span>
  <span class="more" style="left:715px;top:210px">More</span>
  <span class="more" style="left:1096px;top:210px">More</span>
</section>

<div class="testimonial">“testimonial goes here - a very pleased client -testimonial goes here - a very pleased client - ”</div>

<div class="box" style="left:46px;top:1096px;width:311px;height:338px">
  <h2>CONTACT DETAILS</h2>
  <div class="details">
    <h4>HEAD OFFICE</h4>
    <p>42 harrow lane<br>dunmere, eastshire, dn4 7qx.</p>
    <h4>BRANCH OFFICE</h4>
    <p>18 Cedar Court,<br>Lakeview Park, Eastford, EF2 9LB</p>
    <h4 class="tight">E-MAIL</h4>
    <p>info [at] norvanehr [dot] com</p>
    <h4 class="tight">CONTACT #:</h4>
    <p>Tel: 00 220 781<br>Fax: 00 220 782</p>
  </div>
</div>

<div class="box" style="left:447px;top:1096px;width:310px;height:338px">
  <div class="promo" style="margin-top:50px">“IS YOUR COMPANY<br>BREAKING THE LAW?</div>
  <div class="btn-dark" style="left:42px;top:135px;width:223px;height:63px;line-height:63px;font-family:'Questrial',sans-serif;font-weight:400;font-size:25px">CALL US TODAY</div>
  <div class="promo" style="margin-top:100px">AND LET US PROTECT<br>YOUR BUSINESS”</div>
</div>

<div class="box" style="left:837px;top:1096px;width:311px;height:338px">
  <h2>CONTACT FORM</h2>
  <div class="form-sub">Find out now if your business protected</div>
  <span class="field" style="top:90px">Name</span><div class="input" style="top:88px"></div>
  <span class="field" style="top:122px">Email</span><div class="input" style="top:120px"></div>
  <span class="field" style="top:154px">Telephone</span><div class="input" style="top:151px"></div>
  <span class="field" style="top:186px">Comments</span><div class="input" style="top:181px;height:88px"></div>
  <div class="btn-dark" style="left:53px;top:286px;width:93px;height:33px;line-height:33px;font-size:13px">Submit</div>
  <div class="btn-dark" style="left:158px;top:286px;width:93px;height:33px;line-height:33px;font-size:13px">Clear</div>
</div>

<div class="band" style="top:1502px;height:57px;line-height:54px;font-size:13px;letter-spacing:.5px">© NORVANE HR &nbsp;|&nbsp;&nbsp; All Rights Reserved</div>

<!-- ===== Inner page ===== -->
<div class="page-label" style="top:1650px">INNER PAGE</div>

<div class="brand" style="top:1742px">
  <div class="brand-name"><i></i>Norvane HR Ltd</div>
  <div class="brand-tag">Brisk HR Partner</div>
</div>
<div class="call" style="top:1758px">CALL NOW: <b>111 4040 727</b></div>
<nav class="nav" style="top:1832px">
  <a href="#" style="font-weight:700">HOME</a><span class="sep" style="margin:0 4px">|</span>
  <a class="active" href="#">ABOUT US</a><span class="sep">|</span>
  <a href="#">OUR SERVICES</a><span class="sep">|</span>
  <a href="#" style="padding-right:0">CONTACT US</a>
</nav>

<section class="hero" style="top:1872px;height:244px">
  <div class="hero-title" style="top:76px;font-weight:700;font-size:22px;line-height:34px">“12 Years HR Experience -<br>wealth of experience &amp; knowledge”</div>
  <div class="abs" role="img" aria-label="Photo of a group of business people in suits standing together" style="left:455px;top:0;width:745px;height:241px;background:linear-gradient(180deg,#5fb83a,#3e3e3e 55%,#2a2a2a)"></div>
</section>
<div class="crumb">Home &nbsp;&nbsp;-&nbsp;&nbsp; About Us</div>

<main class="about">
  <h1>About Us</h1>
  <p>Lorem Ipsum is simply dummy text of the printing and typesetting industry. Lorem Ipsum has<br>been the industry's standard dummy text ever since the 1500s, when an unknown printer took<br>a galley of type and scrambled it to make a type specimen book. It has survived not only five<br>centuries, but also the leap into electronic typesetting, remaining essentially unchanged. It<br>was popularised in the 1960s with the release of Typeset Press sheets containing Lorem Ipsum<br>passages, and more recently with desktop publishing software like PageForge Studio including<br>versions of Lorem Ipsum.</p>
  <p>Contrary to popular belief, Lorem Ipsum is not simply random text. It has roots in a piece of<br>classical Latin literature from 45 BC, making it over 2000 years old. Dara Fennell, a<br>Latin professor at Larkmoor College in Westvale, looked up one of the more obscure<br>Latin words, consectetur, from a Lorem Ipsum passage, and going through the cites of the<br>word in classical literature, discovered the undoubtable source. Lorem Ipsum comes from<br>sections 1.10.32 and 1.10.33 of "de Rebus Optimis et Pessimis" (The Extremes of Good and<br>Evil) by Marcus Tellan, written in 45 BC. This book is a treatise on the theory of ethics, very<br>popular during the Renaissance. The first line of Lorem Ipsum, "Lorem ipsum dolor sit amet..",<br>comes from a line in section 1.10.32.</p>
  <p>The standard chunk of Lorem Ipsum used since the 1500s is reproduced below for those<br>interested. Sections 1.10.32 and 1.10.33 from "de Rebus Optimis et Pessimis" by Marcus Tellan<br>are also reproduced in their exact original form, accompanied by English versions from the<br>1914 translation by J. Orwin.</p>
</main>

<aside class="box" style="left:837px;top:2224px;width:311px;height:339px">
  <h2>LATEST NEWS/EVENTS</h2>
  <div class="news">
    <p>Lorem Ipsum is simply dummy text of the printing and typesetting industry.</p>
    <p>Lorem Ipsum has been the industry's standard dummy text ever since the 1500s.</p>
    <p>It was popularised in the 1960s.</p>
  </div>
  <span class="more" style="left:220px;top:313px">More</span>
</aside>

<aside class="box" style="left:837px;top:2598px;width:311px;height:337px">
  <h2>CONTACT DETAILS</h2>
  <div class="details">
    <h4>HEAD OFFICE</h4>
    <p>42 harrow lane<br>dunmere, eastshire, dn4 7qx.</p>
    <h4>BRANCH OFFICE</h4>
    <p>18 Cedar Court,<br>Lakeview Park, Eastford, EF2 9LB</p>
    <h4 class="tight">E-MAIL</h4>
    <p>info [at] norvanehr [dot] com</p>
    <h4 class="tight">CONTACT #:</h4>
    <p>Tel: 00 220 781<br>Fax: 00 220 782</p>
  </div>
</aside>

<div class="band" style="top:3091px;height:54px;line-height:52px;font-size:12px">Copyright © 2003-2010 norvanehr-example.com. All Rights Reserved.</div>

</body>
</html>
```